Need a design package for hair towels wrap

We need package design for hair towel wrap ( 3 pack) brand name is The Quorin. We are looking for simple, contemporary and unique design, color palette 2-3 colors. Paper Box size is 9*8*3 inches with PVC window.Actual picture of the product won't be on the package.Attached Brand Logo and description for the package. Barcode needed to be included on the design package.It will be provided later. Attached sample of the box from manufacturer, and instruction for towel wrap which idea I like, if you could make something similar to it, would be great.

Target Market(s)

Zelvora

Industry/Entity Type

Hair

Colors
848484
f5f5f5
faa54b
333333

Requirements
Must have
• Clean, contemporary design.

```html
<!DOCTYPE html>
<html lang="en">
<head>
<meta charset="utf-8">
<title>The Quorin – Microfiber Hair Towel Wrap Packaging</title>
<link rel="stylesheet" href="https://fonts.googleapis.com/css2?family=Playfair+Display:wght@700&family=Raleway:wght@300;400&family=Montserrat:wght@700&display=swap">
<style>
  :root {
    --orange: #f5a24b;
    --charcoal: #333333;
    --grey: #848484;
    --paper: #f5f5f5;
    --white: #ffffff;
    --stage: #e7e4df;
    --gold: #c9a04a;
  }
  * { box-sizing: border-box; margin: 0; padding: 0; }
  html, body { width: 1200px; height: 800px; overflow: hidden; }
  body {
    background: var(--stage);
    display: flex;
    align-items: center;
    justify-content: center;
    gap: 60px;
    font-family: "Raleway", sans-serif;
  }

  /* ---------- Back panel: directions ---------- */
  .panel-back {
    position: relative;
    width: 480px;
    height: 480px;
    background: var(--orange);
    overflow: hidden;
  }
  .panel-back .stripe {
    position: absolute;
    top: 0;
    height: 100%;
    background: var(--paper);
  }
  .panel-back .stripe-a { left: 34px; width: 22px; }
  .panel-back .stripe-b { left: 88px; width: 22px; }
  .panel-back .band {
    position: absolute;
    left: 0;
    width: 100%;
    background: var(--paper);
  }
  .panel-back .band-a { top: 380px; height: 20px; }
  .panel-back .band-b { top: 420px; height: 20px; }
  .panel-back .spec {
    position: absolute;
    left: 150px;
    top: 40px;
    color: var(--paper);
    font-weight: 300;
    font-size: 15px;
    letter-spacing: 0.3px;
  }
  .panel-back .directions-title {
    position: absolute;
    left: 150px;
    top: 92px;
    color: var(--paper);
    font-weight: 300;
    font-size: 17px;
  }
  .steps {
    position: absolute;
    left: 150px;
    top: 132px;
    list-style: none;
    display: flex;
    flex-direction: column;
    gap: 16px;
  }
  .step { display: flex; align-items: center; gap: 16px; }
  .step-figure {
    width: 70px;
    height: 70px;
    border-radius: 50%;
    background: radial-gradient(circle, #ffffff 55%, #ededed 100%);
    border: 1.5px solid #d7d7d7;
  }
  .step-number {
    color: var(--charcoal);
    font-weight: 400;
    font-size: 15px;
  }

  /* ---------- Front panel ---------- */
  .panel-front {
    position: relative;
    width: 560px;
    height: 500px;
    background: var(--white);
    overflow: hidden;
  }
  .panel-front .field {
    position: absolute;
    left: 0; top: 0;
    width: 560px;
    height: 360px;
    background: var(--orange);
  }
  .panel-front .claim-band {
    position: absolute;
    left: 55px; top: 0;
    width: 180px;
    height: 360px;
    background: var(--charcoal);
  }
  .claim {
    position: absolute;
    left: 55px; top: 38px;
    width: 180px;
    text-align: center;
    color: var(--white);
    font-family: "Playfair Display", serif;
    font-weight: 700;
    font-size: 15.5px;
    line-height: 1.3;
  }
  .brand-mark {
    position: absolute;
    left: 119px; top: 205px;
    width: 52px; height: 52px;
    background: var(--gold);
  }
  .brand-name {
    position: absolute;
    left: 20px; top: 315px;
    color: var(--grey);
    font-family: "Montserrat", sans-serif;
    font-weight: 700;
    font-size: 30px;
    letter-spacing: 0.5px;
    white-space: nowrap;
  }
  .window {
    position: absolute;
    left: 270px; top: 32px;
    width: 240px;
    height: 230px;
    background: linear-gradient(160deg, #ffffff 0%, #f1f1f1 60%, #e4e4e4 100%);
  }
  .product-line {
    position: absolute;
    right: 40px; top: 276px;
    text-align: right;
    color: var(--white);
    font-weight: 300;
    font-size: 11px;
    line-height: 1.6;
  }
  .geometry {
    position: absolute;
    left: 0; top: 360px;
  }
</style>
</head>
<body>

  <section class="panel-back" aria-label="Back panel">
    <div class="stripe stripe-a"></div>
    <div class="stripe stripe-b"></div>
    <div class="band band-a"></div>
    <div class="band band-b"></div>
    <p class="spec">Towel Measures 26”x10”</p>
    <p class="directions-title">Directions:</p>
    <ol class="steps">
      <li class="step"><div class="step-figure" role="img" aria-label="Step 1: towel draped over bent-forward head"></div><span class="step-number">1</span></li>
      <li class="step"><div class="step-figure" role="img" aria-label="Step 2: towel twisted over the hair"></div><span class="step-number">2</span></li>
      <li class="step"><div class="step-figure" role="img" aria-label="Step 3: towel wrapped and secured on the head"></div><span class="step-number">3</span></li>
    </ol>
  </section>

  <section class="panel-front" aria-label="Front panel">
    <div class="field"></div>
    <div class="claim-band"></div>
    <p class="claim">The softest,<br>most absorbent,<br>lightest, and<br>safest towel<br>for your<br>beautiful hair.</p>
    <div class="brand-mark"></div>
    <p class="brand-name">THE QUORIN</p>
    <div class="window" role="img" aria-label="Window showing the white microfiber towel"></div>
    <p class="product-line">Microfiber Hair Towel Wrap<br>Set of 3 Hair Towels</p>
    <svg class="geometry" width="560" height="140" viewBox="0 0 560 140">
      <rect x="0" y="0" width="55" height="140" fill="#f5a24b"/>
      <rect x="75" y="30" width="120" height="22" fill="#f5a24b"/>
      <rect x="75" y="80" width="120" height="22" fill="#f5a24b"/>
      <rect x="215" y="0" width="22" height="140" fill="#f5a24b"/>
      <path d="M300 140 V40 H400 V140" fill="none" stroke="#f5a24b" stroke-width="22"/>
      <rect x="440" y="20" width="120" height="22" fill="#f5a24b"/>
      <path d="M560 75 H470 V140" fill="none" stroke="#f5a24b" stroke-width="22"/>
    </svg>
  </section>

</body>
</html>
```